International Container Business Company Needs a Letterhead Design

We need a letterhead design for our company in Hamburg / Germany ( located in the Port ) called RV Kontor GmbH -

www.rv-kontor.de

We have our own logo , please use this one -
We would like to see designs that use the color blue.

RV Kontor GmbH is a young, dynamic and successful company in the container industry.

Our activities cover the following areas:
Container Trade
Container Rental
Container Transport
Maintenance and repair of refrigerated containers
Reefer Service and 24 hour emergency service
Pre Trip Inspection (PTI)
Storage and shipping containers repairs
Depot and terminal service

Industry/Entity Type

Business

Colors
3176b5
0455a3

Requirements
Must have
• The company is acutally called Belsket Handel,
• but we are changing the companies name to
• RV Kontor GmbH ,
• the website will be : www.rv-kontor.de
• and the email is : info@rv-kontor.de
• the rest still same as on the webpage
• thanks

```html
<!DOCTYPE html>
<html lang="de">
<head>
<meta charset="utf-8">
<title>RV Kontor GmbH – Briefbogen</title>
<link rel="stylesheet" href="https://fonts.googleapis.com/css2?family=Open+Sans:wght@400;600&display=swap">
<style>
  :root {
    --brand-blue: #3176b5;
    --deep-blue: #0455a3;
    --paper: #ffffff;
  }
  html, body {
    margin: 0;
    padding: 0;
    overflow: hidden;
    background: var(--paper);
  }
  .letterhead {
    position: relative;
    width: 849px;
    height: 1200px;
    background: var(--paper);
    font-family: "Open Sans", Arial, sans-serif;
    color: var(--brand-blue);
    overflow: hidden;
  }
  .brand-mark {
    position: absolute;
    left: 52px;
    top: 62px;
    display: flex;
    align-items: center;
    gap: 10px;
  }
  .brand-mark__dot {
    width: 26px;
    height: 26px;
    border-radius: 50%;
    background: var(--deep-blue);
  }
  .brand-mark__name {
    font-size: 28px;
    font-weight: 600;
    color: var(--deep-blue);
    letter-spacing: 0.5px;
  }
  .rule {
    position: absolute;
    left: 131px;
    width: 5px;
    background: var(--deep-blue);
  }
  .rule--upper { top: 226px; height: 738px; }
  .rule--lower { top: 1170px; height: 30px; }
  .sender {
    position: absolute;
    left: 90px;
    top: 1000px;
  }
  .sender__name {
    margin: 0;
    font-size: 34px;
    font-weight: 400;
    line-height: 1.2;
    color: var(--brand-blue);
  }
  .sender__address {
    margin: 14px 0 8px 29px;
    font-size: 16px;
    line-height: 1.3;
  }
  .contact-list {
    list-style: none;
    margin: 0;
    padding: 0;
  }
  .contact-list__item {
    display: flex;
    align-items: center;
    gap: 10px;
    height: 22.5px;
    font-size: 15px;
  }
  .contact-list__icon {
    width: 18px;
    height: 18px;
    flex: none;
  }
</style>
</head>
<body>
<main class="letterhead">
  <div class="brand-mark">
    <span class="brand-mark__dot"></span>
    <span class="brand-mark__name">RV Kontor</span>
  </div>

  <div class="rule rule--upper"></div>

  <section class="sender">
    <h1 class="sender__name">RV Kontor GmbH</h1>
    <p class="sender__address">Address Line 01, Adress Line 02.</p>
    <ul class="contact-list">
      <li class="contact-list__item">
        <svg class="contact-list__icon" viewBox="0 0 18 18" aria-hidden="true">
          <circle cx="9" cy="9" r="9" fill="#0455a3"/>
          <path d="M6 5h2l1 2.2-1.2.9a5 5 0 0 0 2.1 2.1l.9-1.2L13 10v2c0 .6-.4 1-1 1A7 7 0 0 1 5 6c0-.6.4-1 1-1z" fill="#fff"/>
        </svg>
        <span>xxx xxx xxxx</span>
      </li>
      <li class="contact-list__item">
        <svg class="contact-list__icon" viewBox="0 0 18 18" aria-hidden="true">
          <circle cx="9" cy="9" r="9" fill="#0455a3"/>
          <rect x="5" y="7" width="8" height="5" rx="1" fill="#fff"/>
          <rect x="6.5" y="4.5" width="5" height="2.5" fill="#fff"/>
        </svg>
        <span>xxx xxx xxxx</span>
      </li>
      <li class="contact-list__item">
        <svg class="contact-list__icon" viewBox="0 0 18 18" aria-hidden="true">
          <circle cx="9" cy="9" r="9" fill="#0455a3"/>
          <rect x="4.5" y="5.5" width="9" height="7" rx="1" fill="#fff"/>
          <path d="M4.8 6l4.2 3.3L13.2 6" stroke="#0455a3" stroke-width="1" fill="none"/>
        </svg>
        <span></span>
      </li>
      <li class="contact-list__item">
        <svg class="contact-list__icon" viewBox="0 0 18 18" aria-hidden="true">
          <circle cx="9" cy="9" r="9" fill="#0455a3"/>
          <circle cx="9" cy="9" r="4.5" fill="none" stroke="#fff" stroke-width="1.2"/>
          <path d="M4.5 9h9M9 4.5c-2 2.5-2 6.5 0 9M9 4.5c2 2.5 2 6.5 0 9" stroke="#fff" stroke-width="1" fill="none"/>
        </svg>
        <span>www.rv-kontor.de</span>
      </li>
    </ul>
  </section>

  <div class="rule rule--lower"></div>
</main>
</body>
</html>
```